Judicial election website to attract voters

I need a simple one-page web design for a judicial election. I'm going to put up one picture, maybe two. The picture I have needs a little touch-up (whiten teeth for example). I have 3 paragraphs of text. I'd like a "Donate" button that can link to a Tillwisp account. I'd also like a little background design, like the Constitution or something like that. There's a couple other little things but that's the bulk of it.

Target Market(s)

Involved voters and some media

Industry/Entity Type

Legal

Number of Pages Required

1 page

Font styles to use
Sans Serif

Requirements
Must have
• My picture, text, donate button
• Phrase "Remember to vote August 30, 2016!"
Nice to have
• Perhaps a second photo, maybe a short 30 second video of me talking directly to the voters, cool background: Constitution, something judgey.
Should not have
• Not sure ... profanity, I guess.

```html
<!DOCTYPE html>
<html lang="en">
<head>
<meta charset="utf-8">
<title>Caroline Margaret Van Holt for Circuit Court Judge</title>
<link rel="stylesheet" href="https://fonts.googleapis.com/css2?family=Roboto+Condensed:wght@700&family=Raleway:wght@300;400;700;800&display=swap">
<style>
  :root {
    --blue: #0b2f9a;
    --ink: #111111;
    --body: #2a2a2a;
    --panel: rgba(255,255,255,0.93);
    --bg-light: #d6d6d6;
    --bg-mid: #b9b9b9;
    --bg-dark: #8f8f8f;
    --footer: #8b1d2c;
    --donate: #c8161d;
  }
  * { box-sizing: border-box; margin: 0; padding: 0; }
  html, body { width: 786px; height: 1200px; overflow: hidden; }
  body { font-family: "Raleway", sans-serif; color: var(--ink); }
  .page { position: relative; width: 786px; height: 1200px; overflow: hidden; }

  .backdrop {
    position: absolute; inset: 0;
    background:
      linear-gradient(115deg, var(--bg-dark) 0%, var(--bg-light) 30%, var(--bg-mid) 45%, var(--bg-light) 60%, #cfcfcf 100%);
  }

  .title-frame { position: absolute; left: 29px; top: 72px; width: 732px; height: 80px; }
  .candidate-name {
    position: absolute; left: 0; right: 0; top: 38px; text-align: center;
    font-family: "Roboto Condensed", sans-serif; font-weight: 700;
    font-size: 62px; line-height: 1; color: var(--blue); letter-spacing: -0.5px;
  }
  .office {
    position: absolute; left: 0; right: 0; top: 126px; text-align: center;
    font-family: "Roboto Condensed", sans-serif; font-weight: 700;
    font-size: 38px; line-height: 1; color: var(--blue);
  }

  .qualities { position: absolute; left: 0; top: 212px; color: var(--blue); font-weight: 800; line-height: 1; }
  .qualities span { position: absolute; white-space: nowrap; }
  .q-dedicated { left: 147px; top: 0; font-size: 54px; }
  .q-experienced { left: 91px; top: 55px; font-size: 36px; font-weight: 700; }
  .q-respected { left: 169px; top: 90px; font-size: 36px; font-weight: 700; }

  .bio {
    position: absolute; left: 60px; width: 333px; top: 354px;
    text-align: right; font-size: 18.8px; line-height: 23.6px; font-weight: 700;
  }
  .bio strong { font-weight: 800; }

  .portrait {
    position: absolute; left: 412px; top: 268px; width: 318px; height: 382px;
    background: radial-gradient(ellipse at 50% 42%, #9c9c9c 0%, #a8a8a8 45%, #c4c4c4 75%, rgba(210,210,210,0) 100%);
  }

  .story {
    position: absolute; left: 56px; top: 650px; width: 674px; height: 350px;
    background: var(--panel); padding: 16px 14px 0;
    text-align: center; font-size: 13.6px; line-height: 17.6px; font-weight: 300; color: var(--body);
  }
  .story p + p { margin-top: 17.6px; }
  .story strong { font-weight: 700; color: var(--ink); }

  .reminder {
    position: absolute; left: 0; right: 0; top: 1024px; text-align: center;
    font-size: 27px; font-weight: 700; color: var(--blue);
  }

  .thanks {
    position: absolute; left: 200px; width: 179px; top: 1077px;
    text-align: right; font-size: 15.5px; line-height: 20px; font-weight: 700;
  }
  .donate { position: absolute; left: 397px; top: 1078px; width: 120px; text-align: center; }
  .donate-button {
    display: block; height: 26px; border-radius: 13px;
    background: linear-gradient(#e1342f, var(--donate) 60%, #9d0f14);
    color: #fff; font-weight: 800; font-size: 18px; line-height: 26px; text-decoration: none;
  }
  .secure { font-size: 7px; font-weight: 700; color: #333; margin-top: 2px; }
  .pay-row { display: flex; align-items: center; justify-content: center; gap: 4px; margin-top: 2px; }
  .pay-name { font-size: 14px; font-weight: 800; color: var(--blue); }
  .badge { width: 12px; height: 8px; background: #8a8a8a; }

  .footer {
    position: absolute; left: 0; right: 0; bottom: 0; height: 46px;
    background: var(--footer); color: #f3e3e5;
    font-size: 10px; font-weight: 400; text-align: center; line-height: 46px;
  }
</style>
</head>
<body>
<main class="page">
  <div class="backdrop" role="img" aria-label="Faded photograph of classical courthouse columns"></div>

  <svg class="title-frame" width="732" height="80" viewBox="0 0 732 80" aria-hidden="true">
    <polyline points="12,0 0,0 0,78 186,78" fill="none" stroke="#0b2f9a" stroke-width="1.5"/>
    <polyline points="710,0 732,0 732,78 548,78" fill="none" stroke="#0b2f9a" stroke-width="1.5"/>
  </svg>
  <h1 class="candidate-name">Caroline Margaret Van Holt</h1>
  <h2 class="office">for Circuit Court Judge</h2>

  <div class="qualities">
    <span class="q-dedicated">Dedicated</span>
    <span class="q-experienced">Experienced</span>
    <span class="q-respected">Respected</span>
  </div>

  <p class="bio">She was born and raised in Tampa Florida, the daughter of an air-conditioning repairman who later opened his own successful business. As the first in her family to go to college, her parents could not have been more proud as she finished her degree at the <strong>Gulf Coast University</strong>, then continued on to <strong>Sunshine State University College of Law</strong> where she graduated with honors.</p>

  <div class="portrait" role="img" aria-label="Portrait photograph of the candidate, smiling"></div>

  <section class="story">
    <p>Dedicating her life to public service in central Florida, she has spent the last <strong>18 years as a prosecutor</strong> fighting for victims of child abuse and sexual abuse in Orange and Osceola counties. She participates in local charities such as the <strong>Harvest Table Food Bank</strong> and the <strong>Adult Reading Alliance</strong>. Caroline shares her knowledge and experience freely, often mentoring the other young prosecutors and lecturing on jury selection and trial strategies. She is also committed to ensuring ethical behavior in the profession of law. She is also committed to ensuring ethical behavior in the profession of law. In law school, she won an award for ethics and professionalism but since then she also served as <strong>Chair of a Regional Bar Grievance Committee</strong>, which handles complaints and ethical violations committed by local attorneys.</p>
    <p>The cornerstone of <strong>Caroline’s candidacy for judge</strong> is her experience in the courtroom. Nobody knows how to run an efficient courtroom better than an attorney who has litigated a hundred felony jury trials and argued more pretrial motions than can be counted. But even a judge with all the right knowledge and experience cannot excel without the correct temperament. Ask any attorney or judge who has worked with Caroline and they will tell you that she treats everyone with respect and handles courtroom surprises with a calm head and sense of humor. She would love your support for judge and the opportunity to use her skills and experience to serve Orange and Osceola County in a new and exciting way.</p>
  </section>

  <p class="reminder">Remember to vote August 30, 2016!</p>

  <p class="thanks">Thank you very much for your contribution</p>
  <div class="donate">
    <a class="donate-button" href="#donate">DONATE</a>
    <div class="secure">Safe &amp; Secure</div>
    <div class="pay-row">
      <span class="pay-name">Tillwisp</span>
      <span class="badge"></span><span class="badge"></span><span class="badge"></span>
    </div>
  </div>

  <footer class="footer">Paid for by the Campaign to Elect Caroline Van Holt for Circuit Court Judge, Circuit 9, Group 14</footer>
</main>
</body>
</html>
```